Brant Ocheltree | Inbound Marketing

Need a logo for a company that fills the need of creating a consistent stream of warm sales leads and revenue (via building of a sales funnel) to companies who either do not have sales teams or use outmoded outbound sales strategy to address the company bottom line. This includes Inbound marketing, SEO, content marketing strategy

Target Market(s)

Small to Medium Size Businesses, who are willing to spend thousands or tens of thousands of dollars on avertising.

Industry/Entity Type

It Company

Contact Information for Business Card

Lumen Inflow | PPC | SEO | Local Social & SEO
512.604.7731
brantocheltree@mailvista.net

Logo Text

Look Inward to Gain Outward

Font styles to use
Sans Serif

Requirements
Nice to have
• I am partial to funnels in natural phenomena (tornados, whirlpools, hurricanes, black holes, spiral galaxies) but this is not a deal breaker. In fact, I don't want to intimidate anybody and seeing photos and artist representation are somewhat unsettling to me as to their vastness and darkness

```html
<!DOCTYPE html>
<html lang="en">
<head>
<meta charset="utf-8">
<title>Lumen Inflow — Business Card</title>
<link rel="stylesheet" href="https://fonts.googleapis.com/css2?family=Oswald:wght@600&family=Open+Sans:wght@400;600;700&display=swap">
<style>
  :root {
    --backdrop: #e6e6e6;
    --navy: #343a85;
    --blue: #2a78c6;
    --silver-light: #ffffff;
    --silver-mid: #e4e5e7;
    --silver-dark: #b9bbbf;
    --logo-grey: #6a6a6a;
    --ink: #2b2b2b;
    --ink-soft: #3f3f3f;
    --white: #ffffff;
  }
  * { box-sizing: border-box; margin: 0; padding: 0; }
  html, body { width: 970px; height: 1200px; overflow: hidden; }
  body { background: var(--backdrop); position: relative; font-family: "Open Sans", Arial, sans-serif; }

  .card {
    position: absolute;
    width: 708px;
    height: 430px;
    overflow: hidden;
    background: linear-gradient(100deg, var(--silver-mid) 0%, var(--silver-light) 40%, var(--silver-light) 60%, var(--silver-mid) 100%);
    box-shadow: 0 4px 14px rgba(0,0,0,0.18);
  }
  .card--front { left: 128px; top: 118px; }
  .card--back { left: 135px; top: 637px; }
  .card__art { position: absolute; inset: 0; }

  .wordmark {
    position: absolute;
    left: 0; right: 0;
    display: flex;
    align-items: center;
    justify-content: center;
    gap: 14px;
    font-family: "Oswald", "Arial Narrow", sans-serif;
    font-weight: 600;
    letter-spacing: 0.5px;
    line-height: 1;
  }
  .wordmark__dot { border-radius: 50%; }
  .card--front .wordmark { top: 112px; font-size: 72px; color: var(--logo-grey); }
  .card--front .wordmark__dot { width: 30px; height: 30px; background: var(--blue); }
  .card--back .wordmark { top: 80px; font-size: 44px; color: var(--white); }
  .card--back .wordmark__dot { width: 20px; height: 20px; background: var(--white); }

  .website {
    position: absolute;
    left: 0; width: 724px; top: 336px;
    text-align: center;
    font-family: "Open Sans", Arial, sans-serif;
    font-weight: 700;
    font-size: 24px;
    letter-spacing: 6px;
    color: var(--white);
  }

  .contact { position: absolute; left: 0; right: 0; top: 222px; color: var(--ink); }
  .contact__name { text-align: center; font-weight: 700; font-size: 20px; margin-left: 72px; color: var(--ink); }
  .contact__services { text-align: center; font-size: 22px; margin-top: 2px; color: var(--ink-soft); margin-left: 0; }
  .contact__list { list-style: none; position: absolute; left: 226px; top: 88px; }
  .contact__item { display: flex; align-items: center; gap: 12px; font-size: 22px; height: 30px; color: var(--ink-soft); }
  .contact__icon { width: 24px; height: 24px; flex: none; }
</style>
</head>
<body>

<section class="card card--front" aria-label="Card front">
  <svg class="card__art" viewBox="0 0 708 430" aria-hidden="true">
    <defs>
      <linearGradient id="bandFront" x1="0" y1="0" x2="0" y2="1">
        <stop offset="0" stop-color="#2a7ccb"/>
        <stop offset="0.45" stop-color="#343a85"/>
        <stop offset="1" stop-color="#343a85"/>
      </linearGradient>
      <linearGradient id="stripeFront" x1="0" y1="0" x2="1" y2="0">
        <stop offset="0" stop-color="#ffffff"/>
        <stop offset="0.5" stop-color="#c8cacd"/>
        <stop offset="0.8" stop-color="#ffffff"/>
        <stop offset="1" stop-color="#9ea1a6"/>
      </linearGradient>
    </defs>
    <path d="M0,262 Q360,236 708,270 L708,430 L0,430 Z" fill="#343a85"/>
    <path d="M0,270 Q360,244 708,280 L708,430 L0,430 Z" fill="url(#bandFront)"/>
    <path d="M0,265 Q360,239 708,273 L708,284 Q360,248 0,278 Z" fill="url(#stripeFront)"/>
  </svg>
  <div class="wordmark"><span>LUMEN</span><span class="wordmark__dot"></span><span>INFLOW</span></div>
  <p class="website">WWW.LUMENINFLOW.COM</p>
</section>

<section class="card card--back" aria-label="Card back">
  <svg class="card__art" viewBox="0 0 708 430" aria-hidden="true">
    <defs>
      <linearGradient id="bandBack" x1="0" y1="0" x2="0" y2="1">
        <stop offset="0" stop-color="#343a85"/>
        <stop offset="0.55" stop-color="#343a85"/>
        <stop offset="1" stop-color="#2a7ccb"/>
      </linearGradient>
      <linearGradient id="stripeBack" x1="0" y1="0" x2="1" y2="0">
        <stop offset="0" stop-color="#ffffff"/>
        <stop offset="0.45" stop-color="#c8cacd"/>
        <stop offset="0.75" stop-color="#ffffff"/>
        <stop offset="1" stop-color="#9ea1a6"/>
      </linearGradient>
    </defs>
    <path d="M0,0 H708 V142 Q354,132 0,140 Z" fill="url(#bandBack)"/>
    <path d="M0,140 Q354,130 708,142 L708,150 Q354,150 0,152 Z" fill="url(#stripeBack)"/>
    <path d="M0,152 Q354,150 708,150 L708,154 Q354,156 0,157 Z" fill="#343a85"/>
  </svg>
  <div class="wordmark"><span>LUMEN</span><span class="wordmark__dot"></span><span>INFLOW</span></div>

  <div class="contact">
    <p class="contact__name">LUMEN INFLOW</p>
    <p class="contact__services">| PPC | SEO | Local Social &amp; SEO</p>
    <ul class="contact__list">
      <li class="contact__item">
        <svg class="contact__icon" viewBox="0 0 24 24" aria-hidden="true">
          <rect x="6" y="2" width="12" height="20" rx="2" fill="none" stroke="#2a5fa8" stroke-width="2"/>
          <line x1="10" y1="18.5" x2="14" y2="18.5" stroke="#2a5fa8" stroke-width="1.5"/>
        </svg>
        <span>512.604.7731</span>
      </li>
      <li class="contact__item">
        <svg class="contact__icon" viewBox="0 0 24 24" aria-hidden="true">
          <rect x="2" y="5" width="20" height="14" fill="none" stroke="#2a5fa8" stroke-width="2"/>
          <path d="M2,5 L12,13 L22,5 M2,19 L9,11 M22,19 L15,11" fill="none" stroke="#2a5fa8" stroke-width="1.6"/>
        </svg>
        <span>brantocheltree@mailvista.net</span>
      </li>
    </ul>
  </div>
</section>

</body>
</html>
```